Kindred Spark is an art based humanitarian project which takes 'at risk' and 'disadvantaged' youths on a life changing humanitarian journey.

Kindred Spark is based in Forster, coastal NSW, however is hoping to expand throughout Australia.

I have a logo and would like it to be predominantly used on the business card.

Kindred Spark uses art as the catalyst to bring together the young adults from across countries. The aim is to help each other heal their hearts through giving.

Could you please add the following to the cards under Kindred Spark::

Changing lives through humanity and art.

Target Market(s)

The target audience will be companies or businesses interested in supporting Kindred Spark. Also, School principals and teachers.

It may help to watch the following trailer about a documentary being made on Kindred Spark: www.fundryvale.com/project/48213‎

Industry/Entity Type

Business

Contact Information for Business Card

Kindred Spark
Tessa Marlowe
Founder

P O BOX 58, Wrenhaven, VIC, 3987
AUSTRALIA
PH 0491328057

paint_spark41@quillmora.net

Logo Text

Kindred Spark

Requirements
Must have
• Must have attached Kindred Spark logo. (I am not sure if this has uploaded on this site????)
Nice to have
• Colour

```html
<!DOCTYPE html>
<html lang="en">
<head>
<meta charset="utf-8">
<title>Kindred Spark – Business Cards</title>
<link href="https://fonts.googleapis.com/css2?family=Patrick+Hand&family=Pacifico&display=swap" rel="stylesheet">
<style>
  :root {
    --stage: #e6e7e9;
    --teal: #4aaebd;
    --pink: #e05b6e;
    --yellow: #f7e53c;
    --ink: #1f1f1f;
    --white: #ffffff;
    --edge: #111111;
    --spark: #e2344d;
  }
  * { margin: 0; padding: 0; box-sizing: border-box; }
  html, body {
    width: 1200px;
    height: 711px;
    overflow: hidden;
    background: var(--stage);
  }
  .card-row {
    display: flex;
    gap: 40px;
    justify-content: center;
    align-items: center;
    width: 1200px;
    height: 711px;
  }
  .card {
    position: relative;
    width: 340px;
    height: 230px;
    border-radius: 12px;
    overflow: hidden;
    background: var(--card-bg);
    box-shadow: 0 2px 8px rgba(0,0,0,.18);
  }
  .card--teal   { --card-bg: var(--teal);   --band: var(--pink);   --name: var(--pink);   --role: var(--white); }
  .card--pink   { --card-bg: var(--pink);   --band: var(--yellow); --name: var(--yellow); --role: var(--white); }
  .card--yellow { --card-bg: var(--yellow); --band: var(--teal);   --name: var(--teal);   --role: var(--ink); }

  .brand {
    position: absolute;
    top: 20px;
    left: 0;
    right: 0;
    display: flex;
    justify-content: center;
    align-items: center;
    gap: 8px;
  }
  .brand__name {
    font-family: "Patrick Hand", cursive;
    font-size: 36px;
    line-height: 38px;
    letter-spacing: 2px;
    text-transform: uppercase;
    text-align: center;
    color: var(--ink);
  }
  .brand__dot {
    width: 14px;
    height: 14px;
    border-radius: 50%;
    background: var(--spark);
  }
  .holder {
    position: absolute;
    top: 108px;
    left: 0;
    right: 0;
    padding-left: 118px;
  }
  .holder__name {
    font-family: "Pacifico", cursive;
    font-size: 15px;
    line-height: 22px;
    color: var(--name);
    text-shadow: 0 0 1px var(--ink), 0 0 1px var(--ink);
  }
  .holder__role {
    font-family: "Patrick Hand", cursive;
    font-size: 15px;
    line-height: 18px;
    color: var(--role);
  }
  .contact {
    position: absolute;
    top: 162px;
    left: 0;
    right: 0;
    text-align: center;
    font-family: "Patrick Hand", cursive;
    font-style: normal;
    font-size: 10px;
    line-height: 11.5px;
    color: var(--ink);
  }
  .band {
    position: absolute;
    left: 0;
    bottom: 0;
    width: 340px;
    height: 46px;
  }
  .band__fill { fill: var(--band); }
  .band__edge { fill: none; stroke: var(--edge); stroke-width: 3; }
</style>
</head>
<body>
<main class="card-row">

  <article class="card card--teal">
    <div class="brand"><span class="brand__name">Kindred<br>Spark</span><span class="brand__dot"></span></div>
    <div class="holder"><p class="holder__name">Tessa Marlowe</p><p class="holder__role">Founder</p></div>
    <address class="contact">P O BOX 58, Wrenhaven, VIC, 3987 Australia<br>PH: 0491 328 057<br>paint_spark41@quillmora.net</address>
    <svg class="band" viewBox="0 0 340 46" aria-hidden="true">
      <path class="band__fill" d="M0 28 C90 20 200 38 340 6 L340 46 L0 46 Z"/>
      <path class="band__edge" d="M0 28 C90 20 200 38 340 6"/>
    </svg>
  </article>

  <article class="card card--pink">
    <div class="brand"><span class="brand__name">Kindred<br>Spark</span><span class="brand__dot"></span></div>
    <div class="holder"><p class="holder__name">Tessa Marlowe</p><p class="holder__role">Founder</p></div>
    <address class="contact">P O BOX 58, Wrenhaven, VIC, 3987 Australia<br>PH: 0491 328 057<br>paint_spark41@quillmora.net</address>
    <svg class="band" viewBox="0 0 340 46" aria-hidden="true">
      <path class="band__fill" d="M0 28 C90 20 200 38 340 6 L340 46 L0 46 Z"/>
      <path class="band__edge" d="M0 28 C90 20 200 38 340 6"/>
    </svg>
  </article>

  <article class="card card--yellow">
    <div class="brand"><span class="brand__name">Kindred<br>Spark</span><span class="brand__dot"></span></div>
    <div class="holder"><p class="holder__name">Tessa Marlowe</p><p class="holder__role">Founder</p></div>
    <address class="contact">P O BOX 58, Wrenhaven, VIC, 3987 Australia<br>PH: 0491 328 057<br>paint_spark41@quillmora.net</address>
    <svg class="band" viewBox="0 0 340 46" aria-hidden="true">
      <path class="band__fill" d="M0 28 C90 20 200 38 340 6 L340 46 L0 46 Z"/>
      <path class="band__edge" d="M0 28 C90 20 200 38 340 6"/>
    </svg>
  </article>

</main>
</body>
</html>
```